Facebook Ad For New online Spectacle Store

We have started a new online store in Australia selling spectacles. As we don't have overheads such as rent electricity etc we are able to do these glasses at an extremely cheap price of $50 for the complete pair. We want to highlight the affordability and quality. This ad will be promoted on Facebook all over Australia. We want to make an impression. There are a lot of people wearing cheap magnifiers from chemists etc that are not suitable as most people need a corrective lens and rarely are both eyes the same power. So it's the people that are buying the $10 glasses we really want to sway to get ones that actually are the correct prescription for them without paying hundreds of dollars on a pair. "Throw away your magnifiers" As it's Facebook we can't really have too much writing in the image HOWEVER we want to highlight COMPLETE GLASSES $50 and that they will be the customers exact power lens. Our Website is www.lumavue.com.au I have uploaded our logo but you do not need it in the design. We will be adding text to the Ad but not in the image you design (except for complete glasses for $50). you can take some of the images of frames from the website or I can upload just ask- tell me which one suits your design. Basically you have freedom to come up with something that will impress our potential customers make them click the link and check out our website.

Target Market(s)

People that use Cheap magnifiers - our glasses are a upgrade and better for their eyes

Industry/Entity Type

Eyewear

Colors

Designer to choose colors to be used in the design.

Requirements
Must have
• Complete Glasses $50 (Plus postage)- The (plus postage) in smaller writing than the Complete glasses for $50 part

```html
<!DOCTYPE html>
<html lang="en">
<head>
<meta charset="utf-8">
<title>Lumavue – Affordable Prescription Glasses</title>
<link rel="stylesheet" href="https://fonts.googleapis.com/css2?family=Luckiest+Guy&family=Alfa+Slab+One&family=Bangers&family=Arimo:wght@400&display=swap">
<style>
  :root {
    --sky: #6aaed6;
    --white: #ffffff;
    --ink: #1b1b1b;
    --outline: #3a2a2a;
    --orange: #ff8a2a;
    --pink: #ff4fa8;
    --red: #e0101a;
    --purple: #7a2cff;
  }
  * { margin: 0; padding: 0; box-sizing: border-box; }
  html, body { width: 1200px; height: 628px; overflow: hidden; background: var(--white); }
  .ad {
    position: relative;
    width: 1200px;
    height: 628px;
    overflow: hidden;
    font-family: "Arimo", Arial, sans-serif;
  }
  .ad__backdrop { position: absolute; inset: 0; }

  .headline {
    position: absolute;
    left: 38px;
    top: 10px;
    font-family: "Luckiest Guy", "Bangers", "Impact", sans-serif;
    font-weight: 400;
    font-size: 48px;
    line-height: 54px;
    letter-spacing: 1px;
    text-transform: uppercase;
    background: linear-gradient(90deg, #7a2cff 0%, #d21ee0 30%, #ff2a6a 62%, #ff7a1a 100%);
    -webkit-background-clip: text;
    background-clip: text;
    color: transparent;
  }

  .tagline {
    position: absolute;
    left: 170px;
    top: 128px;
    width: 420px;
    text-align: center;
    font-family: "Alfa Slab One", Georgia, serif;
    font-size: 32px;
    line-height: 46px;
    text-transform: uppercase;
    color: var(--white);
    text-shadow: 0 2px 3px rgba(0, 0, 0, 0.25);
  }

  .footnote {
    position: absolute;
    right: 12px;
    top: 6px;
    font-size: 13px;
    color: var(--ink);
  }

  .warning {
    position: absolute;
    left: 700px;
    top: 52px;
    width: 440px;
    text-align: center;
    font-family: "Bangers", "Impact", sans-serif;
    font-size: 44px;
    line-height: 56px;
    letter-spacing: 1px;
    transform: rotate(-10deg);
    -webkit-text-stroke: 1.5px var(--outline);
  }
  .warning .line--orange { color: var(--orange); }
  .warning .line--pink { color: var(--pink); }

  .offer {
    position: absolute;
    font-family: "Alfa Slab One", Georgia, serif;
    text-align: center;
    transform: rotate(-8deg);
    -webkit-text-stroke: 1.2px var(--outline);
  }
  .offer--savings {
    left: 10px;
    top: 352px;
    width: 480px;
    font-size: 31px;
    line-height: 40px;
    color: var(--orange);
  }
  .offer--price {
    left: 40px;
    top: 455px;
    width: 420px;
    font-size: 31px;
    line-height: 40px;
    color: var(--pink);
  }

  .deal {
    position: absolute;
    left: 505px;
    top: 232px;
    width: 260px;
    text-align: center;
    font-family: "Bangers", "Impact", sans-serif;
    transform: rotate(-6deg);
  }
  .deal__main {
    display: block;
    font-size: 32px;
    line-height: 34px;
    letter-spacing: 1px;
    color: var(--purple);
    -webkit-text-stroke: 1px var(--outline);
  }
  .deal__note {
    display: block;
    font-family: "Arimo", Arial, sans-serif;
    font-size: 15px;
    line-height: 20px;
    color: var(--ink);
  }

  .product-shot {
    position: absolute;
    left: 492px;
    top: 300px;
    width: 650px;
    height: 280px;
  }

  .web-address {
    position: absolute;
    right: 20px;
    bottom: 12px;
    font-size: 22px;
    color: var(--red);
  }
</style>
</head>
<body>
<main class="ad">
  <svg class="ad__backdrop" width="1200" height="628" viewBox="0 0 1200 628" aria-hidden="true">
    <defs>
      <linearGradient id="sunny-field" x1="0" y1="0" x2="1" y2="0">
        <stop offset="0" stop-color="#f6f21c"/>
        <stop offset="0.45" stop-color="#8cf03c"/>
        <stop offset="1" stop-color="#22ee78"/>
      </linearGradient>
      <radialGradient id="mint-glow" cx="0.78" cy="0.42" r="0.6">
        <stop offset="0" stop-color="#f2fffa"/>
        <stop offset="0.5" stop-color="#8ff8cc"/>
        <stop offset="1" stop-color="#1ff08a"/>
      </radialGradient>
    </defs>
    <rect width="1200" height="628" fill="var(--sky)"/>
    <path d="M560 0 H1200 V520 C1120 500 1010 520 960 628 H370 C420 380 470 160 560 0 Z" fill="url(#mint-glow)"/>
    <path d="M0 130 C140 110 300 150 420 250 C520 340 560 480 540 628 H0 Z" fill="url(#sunny-field)"/>
  </svg>

  <h1 class="headline">Best Quality Glasses<br>Most Affordable Prices</h1>
  <p class="tagline">Throw Away Your<br>Magnifiers</p>
  <p class="footnote">*not suitable as rarely both eyes are same power</p>

  <p class="warning">
    <span class="line--orange">Your 10 Dollar Glasses</span><br>
    <span class="line--pink">Are Not Good For</span><br>
    <span class="line--pink">Your Precious Eyes*</span>
  </p>

  <p class="deal">
    <span class="deal__main">Complete Glasses $50</span>
    <span class="deal__note">(plus postage)</span>
  </p>

  <p class="offer offer--savings">NO NEED TO PAY 100S<br>OF DOLLARS FOR SPECS</p>
  <p class="offer offer--price">GET YOUR SPECS<br>@ STARTING PRICE<br>OF 50 DOLLARS</p>

  <svg class="product-shot" viewBox="0 0 650 280" role="img" aria-label="Product photo of tortoiseshell rectangular spectacle frames">
    <defs>
      <linearGradient id="frame-tone" x1="0" y1="0" x2="0" y2="1">
        <stop offset="0" stop-color="#3d3540"/>
        <stop offset="0.5" stop-color="#8a6a48"/>
        <stop offset="1" stop-color="#d8b47a"/>
      </linearGradient>
    </defs>
    <rect x="0" y="60" width="650" height="220" rx="60" fill="url(#frame-tone)" opacity="0.45"/>
  </svg>

  <p class="web-address">www.lumavue.com.au</p>
</main>
</body>
</html>
```